Biz Card for Marla Dempsey Insurance Agency
Biz Card for Marla Dempsey Insurance Agency - Financial Services
Creative Brief
Bright & Fun-filled
Marla Dempsey
Independent Agent
Clemmons, NC
office 336-521-0974
cell 336-597-2160
marladempsey34@qorvinmail.com
please include her picture in her new card. I will also upload a copy of what we are currently using. she needs something new and fresh. please use the new logo we upload.
Also, please see the words we are using for the back of her card, please use those same words on the new cards.

```html
<!DOCTYPE html>
<html lang="en">
<head>
<meta charset="utf-8">
<title>Marla Dempsey Insurance Agency – Stationery Concepts</title>
<link href="https://fonts.googleapis.com/css2?family=Cinzel:wght@700&family=Open+Sans:wght@400;600;700&display=swap" rel="stylesheet">
<style>
  :root {
    --board: #3a3d41;
    --board-dark: #2e3034;
    --navy: #1f3f7a;
    --navy-deep: #17305e;
    --green: #2f9a3c;
    --green-light: #8cc63f;
    --paper: #ffffff;
    --ink: #4a4f55;
    --muted: #9aa0a6;
    --wash: #e6f1e4;
  }
  * { box-sizing: border-box; margin: 0; padding: 0; }
  html, body { width: 1200px; height: 382px; overflow: hidden; }
  body {
    background: radial-gradient(circle at 30% 40%, var(--board) 0%, var(--board-dark) 100%);
    font-family: "Open Sans", Arial, sans-serif;
    color: var(--ink);
    position: relative;
  }
  .sheet { position: absolute; background: var(--paper); overflow: hidden; box-shadow: 0 2px 6px rgba(0,0,0,.45); }
  .wordmark { font-family: "Cinzel", Georgia, serif; font-weight: 700; letter-spacing: .04em; white-space: nowrap; }
  .mark-dot { display: inline-block; border-radius: 50%; background: var(--green); }
  .wave { position: absolute; left: 0; bottom: 0; width: 100%; display: block; }
  .caption { position: absolute; font-size: 7px; color: var(--muted); }

  /* Brand block */
  .brand { position: absolute; left: 14px; top: 18px; width: 225px; text-align: center; color: var(--paper); }
  .brand .mark-dot { width: 56px; height: 56px; border: 3px solid #4c5157; }
  .brand .wordmark { font-size: 22px; margin-top: 8px; color: var(--paper); }
  .brand .agency { font-size: 8px; letter-spacing: .25em; color: var(--green-light); font-weight: 600; }
  .brand .concepts { font-size: 9px; color: #c8ccd0; margin-top: 6px; }

  /* Business cards */
  .card { left: 14px; width: 222px; height: 88px; }
  .card-front { top: 148px; }
  .card-back { top: 250px; }
  .card .tagline { position: absolute; left: 10px; top: 12px; width: 110px; font-size: 6px; line-height: 1.5; color: var(--navy); font-weight: 600; }
  .card .logo-lockup { position: absolute; right: 12px; top: 12px; text-align: center; width: 90px; }
  .logo-lockup .mark-dot { width: 20px; height: 20px; }
  .logo-lockup .wordmark { font-size: 8px; color: var(--navy); margin-top: 3px; }
  .logo-lockup .agency { font-size: 4.5px; letter-spacing: .2em; color: var(--green); font-weight: 600; white-space: nowrap; }
  .card-back .panel { position: absolute; left: 0; top: 0; width: 92px; height: 100%; background: var(--navy); padding: 10px; }
  .card-back .panel li { list-style: none; font-size: 6.5px; color: var(--paper); line-height: 1.6; }
  .card-back .panel li::before { content: ""; display: inline-block; width: 4px; height: 4px; background: var(--green-light); border-radius: 50%; margin-right: 5px; vertical-align: middle; }
  .portrait { position: absolute; width: 26px; height: 32px; background: linear-gradient(#b8a596, #6f5e52); }
  .card-back .portrait { left: 100px; top: 12px; }
  .card-back .details { position: absolute; left: 132px; top: 12px; width: 84px; font-size: 4.6px; line-height: 1.55; color: var(--ink); white-space: nowrap; }
  .card-back .details strong { color: var(--navy); font-size: 6px; display: block; }

  /* Letterheads */
  .letterhead { top: 19px; width: 282px; height: 328px; }
  .lh-first { left: 254px; }
  .lh-second { left: 560px; }
  .letterhead .logo-lockup { position: absolute; left: 18px; top: 16px; text-align: center; width: 90px; }
  .letterhead .contact { position: absolute; right: 16px; top: 18px; font-size: 5px; line-height: 1.6; text-align: right; color: var(--ink); }
  .letterhead .watermark { position: absolute; left: 40px; top: 140px; width: 200px; height: 140px; background: radial-gradient(ellipse at 50% 50%, var(--wash) 0%, rgba(230,241,228,0) 70%); }

  /* Envelopes */
  .envelope { left: 870px; width: 322px; }
  .env-green { top: 19px; height: 106px; }
  .env-navy { top: 132px; height: 106px; }
  .env-plain { top: 245px; height: 48px; }
  .env-small { top: 298px; height: 48px; left: 912px; width: 236px; }
  .flap { position: absolute; left: 0; top: 0; width: 100%; display: block; }
  .envelope .logo-lockup { position: absolute; left: 12px; width: 60px; text-align: center; }
  .envelope .logo-lockup .mark-dot { width: 12px; height: 12px; }
  .envelope .logo-lockup .wordmark { font-size: 5px; }
  .envelope .logo-lockup .agency { font-size: 3px; }
  .envelope .seal { position: absolute; left: 50%; transform: translateX(-50%); width: 16px; height: 16px; border-radius: 50%; background: var(--paper); }
</style>
</head>
<body>

<header class="brand">
  <span class="mark-dot"></span>
  <div class="wordmark">MARLA DEMPSEY</div>
  <div class="agency">INSURANCE AGENCY</div>
  <div class="concepts">Stationary Concepts</div>
</header>

<section class="sheet card card-front">
  <p class="tagline">Protecting what matters most to you and your family</p>
  <div class="logo-lockup">
    <span class="mark-dot"></span>
    <div class="wordmark">MARLA DEMPSEY</div>
    <div class="agency">INSURANCE AGENCY</div>
  </div>
  <svg class="wave" viewBox="0 0 100 20" preserveAspectRatio="none" height="18">
    <path d="M0 12 Q50 2 100 8 L100 20 L0 20Z" fill="var(--green)"/>
    <path d="M0 15 Q50 7 100 12 L100 20 L0 20Z" fill="var(--navy)"/>
  </svg>
</section>
<span class="caption" style="left:14px;top:238px">Business Card Front</span>

<section class="sheet card card-back">
  <ul class="panel">
    <li>Auto</li><li>Home</li><li>Life</li><li>Business</li><li>Health</li>
  </ul>
  <div class="portrait" role="img" aria-label="Portrait photo of Marla Dempsey"></div>
  <div class="details">
    <strong>Marla Dempsey</strong>
    Independent Agent<br>
    Clemmons, NC<br>
    office 336-521-0974<br>
    cell 336-597-2160<br>
    marladempsey34@qorvinmail.com
  </div>
  <svg class="wave" viewBox="0 0 100 20" preserveAspectRatio="none" height="10">
    <path d="M0 14 Q50 6 100 10 L100 20 L0 20Z" fill="var(--green)"/>
  </svg>
</section>
<span class="caption" style="left:14px;top:340px">Business Card Back</span>

<section class="sheet letterhead lh-first">
  <div class="logo-lockup">
    <span class="mark-dot"></span>
    <div class="wordmark">MARLA DEMPSEY</div>
    <div class="agency">INSURANCE AGENCY</div>
  </div>
  <div class="contact">
    Clemmons, NC<br>office 336-521-0974<br>cell 336-597-2160<br>marladempsey34@qorvinmail.com
  </div>
  <div class="watermark" role="img" aria-label="Faint decorative illustration area"></div>
  <svg class="wave" viewBox="0 0 100 20" preserveAspectRatio="none" height="34">
    <path d="M0 10 Q50 0 100 6 L100 20 L0 20Z" fill="var(--green)"/>
    <path d="M0 14 Q50 6 100 11 L100 20 L0 20Z" fill="var(--navy)"/>
  </svg>
</section>
<span class="caption" style="left:254px;top:350px">Letterhead</span>

<section class="sheet letterhead lh-second">
  <div class="logo-lockup">
    <span class="mark-dot"></span>
    <div class="wordmark">MARLA DEMPSEY</div>
    <div class="agency">INSURANCE AGENCY</div>
  </div>
  <div class="watermark" role="img" aria-label="Faint decorative illustration area"></div>
  <svg class="wave" viewBox="0 0 100 20" preserveAspectRatio="none" height="34">
    <path d="M0 10 Q50 0 100 6 L100 20 L0 20Z" fill="var(--green)"/>
    <path d="M0 14 Q50 6 100 11 L100 20 L0 20Z" fill="var(--navy)"/>
  </svg>
</section>
<span class="caption" style="left:560px;top:350px">Second Page</span>

<section class="sheet envelope env-green">
  <svg class="flap" viewBox="0 0 100 30" preserveAspectRatio="none" height="38">
    <path d="M0 0 H100 V18 Q50 34 0 18Z" fill="var(--green)"/>
  </svg>
  <span class="seal" style="top:18px"></span>
</section>

<section class="sheet envelope env-navy">
  <svg class="flap" viewBox="0 0 100 30" preserveAspectRatio="none" height="46">
    <path d="M0 0 H100 V18 Q50 34 0 18Z" fill="var(--navy)"/>
  </svg>
  <span class="seal" style="top:20px"></span>
</section>

<section class="sheet envelope env-plain">
  <div class="logo-lockup" style="top:6px">
    <span class="mark-dot"></span>
    <div class="wordmark">MARLA DEMPSEY</div>
    <div class="agency">INSURANCE AGENCY</div>
  </div>
</section>

<section class="sheet envelope env-small">
  <div class="logo-lockup" style="top:6px">
    <span class="mark-dot"></span>
    <div class="wordmark">MARLA DEMPSEY</div>
    <div class="agency">INSURANCE AGENCY</div>
  </div>
</section>

</body>
</html>
```